Tamkor, a service provider dedicated to improving the performance of a website

Tamkor offers optimization and performance improvement for all types of websites (showcase sites, e-commerce, ...), with the aim of improving their ranking on Vintrel and their customer transformation rate. The main benefits consist in optimizing the factors of a site. In addition, we also offer content creation (description of product sheets, services, ...), Vintrel Ads campaign management, migration version for Prestashop / Wordpress, etc. The design must be a fresh image, dynamic, why not "fun", but also serious. No favorite color, carte blanche on this point;)

```html
<!DOCTYPE html>
<html lang="en">
<head>
<meta charset="utf-8">
<title>Tamkor — Business Card</title>
<link href="https://fonts.googleapis.com/css2?family=Signika:wght@700&family=Roboto:ital,wght@1,400;1,700&display=swap" rel="stylesheet">
<style>
  :root {
    --brand-blue: #344c94;
    --brand-blue-light: #3d57a3;
    --brand-blue-deep: #2c4286;
    --paper: #efefef;
    --paper-accent: #dcdeea;
    --backdrop: #e6e6e6;
    --ink: #4a4a4a;
    --white: #f4f4f4;
  }
  * { margin: 0; padding: 0; box-sizing: border-box; }
  html, body {
    width: 1200px; height: 1200px; overflow: hidden;
    background: var(--backdrop);
  }
  .stage { position: relative; width: 1200px; height: 1200px; }

  .card {
    position: absolute; left: 227px; width: 746px; height: 426px;
    overflow: hidden;
  }
  .card--front { top: 135px; background: var(--brand-blue); }
  .card--back { top: 639px; background: var(--paper); }

  .accent-circle { position: absolute; border-radius: 50%; }
  .card--front .accent-circle {
    left: -150px; top: 40px; width: 480px; height: 480px;
    background: linear-gradient(160deg, var(--brand-blue-light) 0%, var(--brand-blue) 45%, var(--brand-blue-deep) 100%);
    box-shadow: inset 3px 4px 0 rgba(255,255,255,0.08), inset -3px -4px 0 rgba(0,0,0,0.08);
  }
  .card--back .accent-circle {
    right: -120px; bottom: -170px; width: 380px; height: 380px;
    background: var(--paper-accent);
    opacity: 0.8;
  }

  .wordmark {
    position: absolute;
    font-family: "Signika", sans-serif;
    font-weight: 700;
    font-size: 100px;
    line-height: 1;
    letter-spacing: -1px;
  }
  .card--front .wordmark { right: 80px; top: 260px; color: var(--white); }
  .card--back .wordmark { left: 54px; top: 46px; color: var(--brand-blue); }

  .brand-square {
    position: absolute; left: 577px; top: 46px;
    width: 109px; height: 109px; border-radius: 24px;
    background: linear-gradient(135deg, var(--brand-blue-light) 0%, var(--brand-blue) 50%, var(--brand-blue-deep) 100%);
  }

  .address, .contacts, .person {
    position: absolute;
    font-family: "Roboto", sans-serif;
    font-style: italic;
    color: var(--ink);
    font-size: 19px;
  }
  .address { left: 54px; top: 222px; line-height: 25.5px; }
  .contacts { left: 54px; top: 284px; list-style: none; }
  .contacts li {
    display: flex; align-items: center; gap: 8px; height: 25.3px;
  }
  .contact-icon { width: 19px; height: 19px; flex: none; }

  .person { right: 60px; top: 338px; text-align: right; line-height: 22px; z-index: 1; }
  .person-name {
    font-weight: 700; font-size: 20px; color: var(--brand-blue);
    text-transform: uppercase; letter-spacing: 0.2px;
  }
</style>
</head>
<body>
<main class="stage">

  <section class="card card--front">
    <div class="accent-circle" aria-hidden="true"></div>
    <div class="wordmark">Tamkor</div>
  </section>

  <section class="card card--back">
    <div class="accent-circle" aria-hidden="true"></div>
    <div class="wordmark">Tamkor</div>
    <div class="brand-square"></div>

    <p class="address">Harbor Row 48, Suite 12<br>Zip &amp; Country Code</p>

    <ul class="contacts">
      <li>
        <svg class="contact-icon" viewBox="0 0 20 20" aria-hidden="true">
          <circle cx="10" cy="10" r="10" fill="#344c94"/>
          <path d="M6.5 5.2l1.8-.4 1 2.4-1.1.9a6 6 0 0 0 3 3l.9-1.1 2.4 1-.4 1.8c-4.2.4-8-3.4-7.6-7.6z" fill="#fff"/>
        </svg>
        <span>(555) 214-7730</span>
      </li>
      <li>
        <svg class="contact-icon" viewBox="0 0 20 20" aria-hidden="true">
          <circle cx="10" cy="10" r="10" fill="#344c94"/>
          <rect x="7" y="4.5" width="6" height="3" fill="#fff"/>
          <rect x="5" y="8" width="10" height="5" rx="1" fill="#fff"/>
          <rect x="7" y="11.5" width="6" height="4" fill="#fff" stroke="#344c94" stroke-width=".8"/>
        </svg>
        <span>(555) 214-7731</span>
      </li>
      <li>
        <svg class="contact-icon" viewBox="0 0 20 20" aria-hidden="true">
          <circle cx="10" cy="10" r="10" fill="#344c94"/>
          <rect x="5" y="6.5" width="10" height="7" fill="#fff"/>
          <path d="M5 6.5l5 4 5-4" fill="none" stroke="#344c94" stroke-width="1"/>
        </svg>
        <span>hello@tamkor.example</span>
      </li>
      <li>
        <svg class="contact-icon" viewBox="0 0 20 20" aria-hidden="true">
          <circle cx="10" cy="10" r="10" fill="#344c94"/>
          <g fill="none" stroke="#fff" stroke-width="1">
            <circle cx="10" cy="10" r="5"/>
            <ellipse cx="10" cy="10" rx="2.2" ry="5"/>
            <path d="M5 10h10M6 7.5h8M6 12.5h8"/>
          </g>
        </svg>
        <span>www.tamkor.example</span>
      </li>
    </ul>

    <div class="person">
      <div class="person-name">Marcus Lindqvist</div>
      <div class="person-title">Founder &amp; CEO</div>
    </div>
  </section>

</main>
</body>
</html>
```